Stainless Steel Water Bottle Packaging

We need a design for our cylindrical water bottle packaging.

Please see attached template (500ml cola bottle template .ai file) for exact dimensions.

VOLO is defined as the elemental forces of nature embodied in an object or person. The design should be eye catching and draw potential clients in. Although its a cylindrical bottle/box, the front which would face the customer when sitting on a shelf should clearly display our logo.

Requirements
Must have
• Designed to the specifications of the attached template (see attached)
• Our VOLO Logo (see attached) and website www.volobottle.com(in smaller font) must appear.
• Size of bottle must appear - '17 oz/500 ml'
• These should appear somewhere:
• 'INULATED DOUBLE-WALL STAINLESS STEEL WATER BOTTLE'
• 'VOLO Bottles magically keeps drinks cold for up to 24hrs, hot for 12',
• 'BPA Free'
• 'For every VOLO bottle purchased, a portion of proceeds will go towards charity. Each of our colour's have been assigned a specific charity. Please visit www.volobottle.com to find out which charity you helped support!'
• The Top circle - just our Symbol (flame/drop)
• The bottom circle - 'Inc. Designed in Canada made in China' on the outer edge leaving the middle empty for the UPC code.
• Reference website for the bottle case I'm looking for:
• http://shopcorventi.com/t-dune-lagoon-coral-insulated-water-bottle
Nice to have
• illustration of our water bottle shape (see attached) appearing somewhere on the box is something i had in mind but definitely not necessary.

```html
<!DOCTYPE html>
<html lang="en">
<head>
<meta charset="utf-8">
<title>VOLO Bottle Packaging Dieline</title>
<link href="https://fonts.googleapis.com/css2?family=Arimo&family=Montserrat:wght@400;600;700&display=swap" rel="stylesheet">
<style>
  :root {
    --brand-blue: #35a6d8;
    --band-light: #86c9e7;
    --dieline-red: #e0383e;
    --guide-ink: #222222;
    --paper: #ffffff;
  }
  html, body {
    margin: 0;
    padding: 0;
    width: 1000px;
    height: 1200px;
    overflow: hidden;
    background: var(--paper);
  }
  .artboard {
    position: relative;
    width: 1000px;
    height: 1200px;
    font-family: "Montserrat", sans-serif;
  }
  .artboard svg.dieline {
    position: absolute;
    left: 0;
    top: 0;
  }
  .spec-label {
    position: absolute;
    font-family: "Arimo", Arial, sans-serif;
    font-size: 31px;
    color: #111;
    white-space: nowrap;
    letter-spacing: -0.6px;
  }
  .dim-label {
    position: absolute;
    font-family: "Arimo", Arial, sans-serif;
    font-size: 14px;
    color: var(--guide-ink);
    white-space: nowrap;
  }
  .dim-label.bleed { color: var(--dieline-red); }
  .dim-label.vertical {
    transform: translate(-50%, -50%) rotate(-90deg);
    background: var(--paper);
    padding: 0 3px;
  }
  .charity-copy {
    position: absolute;
    left: 262px;
    top: 490px;
    width: 136px;
    color: var(--brand-blue);
    font-size: 10.3px;
    line-height: 13px;
    text-align: justify;
  }
  .charity-copy .site-url {
    font-weight: 700;
    font-size: 11.5px;
    margin: 0 0 18px;
    text-align: left;
  }
  .charity-copy p { margin: 0 0 13px; }
  .charity-copy .visit { text-align: left; }
  .brand-name {
    position: absolute;
    left: 487px;
    top: 580px;
    transform: translate(-50%, -50%) rotate(-90deg);
    font-weight: 700;
    font-size: 96px;
    letter-spacing: 22px;
    color: var(--brand-blue);
    white-space: nowrap;
    line-height: 1;
  }
  .cap-brand {
    font-family: "Montserrat", sans-serif;
    font-weight: 700;
    font-size: 34px;
    fill: var(--brand-blue);
    letter-spacing: 2px;
  }
  .volume {
    position: absolute;
    left: 485px;
    top: 866px;
    transform: translateX(-50%);
    font-size: 19px;
    color: var(--brand-blue);
    white-space: nowrap;
  }
  .product-line {
    position: absolute;
    left: 485px;
    top: 902px;
    transform: translateX(-50%);
    text-align: center;
    font-size: 13px;
    line-height: 16px;
    letter-spacing: 0.6px;
    color: var(--brand-blue);
    white-space: nowrap;
  }
  .promise {
    position: absolute;
    left: 699px;
    top: 610px;
    transform: translate(-50%, -50%) rotate(-90deg);
    text-align: center;
    font-weight: 700;
    font-size: 17.5px;
    line-height: 21px;
    color: var(--paper);
    white-space: nowrap;
  }
  .bpa-badge {
    position: absolute;
    left: 262px;
    top: 808px;
    width: 42px;
    height: 42px;
    border: 1.5px solid var(--brand-blue);
    border-radius: 50%;
    color: var(--brand-blue);
    font-weight: 700;
    font-size: 10.5px;
    line-height: 11px;
    display: flex;
    align-items: center;
    justify-content: center;
    text-align: center;
  }
  .bottle-icon {
    position: absolute;
    left: 316px;
    top: 786px;
    width: 20px;
    height: 74px;
    background: var(--brand-blue);
    border-radius: 6px 6px 4px 4px;
  }
</style>
</head>
<body>
<div class="artboard">

  <div class="spec-label" style="left:148px; top:80px;">cap’s diameter 7.8cm</div>
  <div class="spec-label" style="left:486px; top:80px;">the bottom</div>

  <svg class="dieline" width="1000" height="1200" viewBox="0 0 1000 1200">
    <defs>
      <path id="bottom-arc" d="M476,226 A67,67 0 0 1 610,226"/>
      <linearGradient id="side-band-fill" x1="0" y1="0" x2="1" y2="0">
        <stop offset="0" stop-color="var(--band-light)"/>
        <stop offset="0.3" stop-color="var(--brand-blue)"/>
        <stop offset="1" stop-color="var(--brand-blue)"/>
      </linearGradient>
    </defs>

    <!-- cap top circle -->
    <circle cx="360" cy="238" r="85" fill="none" stroke="var(--dieline-red)" stroke-width="1"/>
    <text class="cap-brand" x="360" y="250" text-anchor="middle">VOLO</text>

    <!-- bottom circle -->
    <circle cx="543" cy="238" r="85" fill="none" stroke="var(--dieline-red)" stroke-width="1"/>
    <text font-family="Montserrat, sans-serif" font-weight="700" font-size="8.5" fill="var(--brand-blue)">
      <textPath href="#bottom-arc" startOffset="50%" text-anchor="middle">Inc. Designed in Canada made in China</textPath>
    </text>
    <circle cx="487" cy="226" r="5" fill="none" stroke="var(--dieline-red)" stroke-width="1"/>
    <circle cx="602" cy="226" r="5" fill="none" stroke="var(--dieline-red)" stroke-width="1"/>

    <!-- side colour band -->
    <rect x="600" y="356" width="171" height="603" fill="url(#side-band-fill)" role="img" aria-label="Decorative two-tone blue water wave artwork"/>

    <!-- dieline frame -->
    <rect x="200" y="334" width="571" height="647" fill="none" stroke="var(--dieline-red)" stroke-width="1"/>
    <line x1="221" y1="334" x2="221" y2="981" stroke="var(--dieline-red)" stroke-width="1"/>
    <line x1="221" y1="356" x2="771" y2="356" stroke="var(--dieline-red)" stroke-width="1"/>
    <line x1="221" y1="959" x2="771" y2="959" stroke="var(--dieline-red)" stroke-width="1"/>

    <!-- brand dot -->
    <circle cx="487" cy="812" r="16" fill="var(--brand-blue)"/>

    <!-- dimension guides -->
    <g stroke="var(--guide-ink)" stroke-width="0.8">
      <line x1="150" y1="334" x2="150" y2="981"/>
      <line x1="138" y1="334" x2="162" y2="334"/>
      <line x1="138" y1="356" x2="162" y2="356"/>
      <line x1="138" y1="470" x2="162" y2="470"/>
      <line x1="138" y1="959" x2="162" y2="959"/>
      <line x1="138" y1="981" x2="162" y2="981"/>
      <line x1="200" y1="1012" x2="771" y2="1012"/>
      <line x1="200" y1="1002" x2="200" y2="1024"/>
      <line x1="221" y1="1002" x2="221" y2="1024"/>
      <line x1="771" y1="1002" x2="771" y2="1024"/>
    </g>
  </svg>

  <div class="dim-label bleed" style="left:117px; top:340px;">10.00mm</div>
  <div class="dim-label vertical" style="left:150px; top:413px;">55.00mm</div>
  <div class="dim-label vertical" style="left:150px; top:720px;">220.00mm</div>
  <div class="dim-label bleed" style="left:117px; top:962px;">10.00mm</div>
  <div class="dim-label" style="left:166px; top:1027px;">10.00mm</div>
  <div class="dim-label" style="left:396px; top:1028px; font-size:15px;">8X3.14159=251.327mm</div>

  <section class="charity-copy">
    <p class="site-url">www.volobottle.com</p>
    <p>For every VOLO bottle purchased, a portion of proceeds will go towards charity.<br>Each of our colour’s have been assigned a specific charity.</p>
    <p class="visit">Please visit:<br>www.volobottle.com<br>to find out which charity you helped support!</p>
  </section>

  <div class="brand-name">VOLO</div>

  <div class="bpa-badge">BPA<br>FREE</div>
  <div class="bottle-icon" role="img" aria-label="Silhouette of the VOLO water bottle"></div>

  <div class="volume">17 oz/500 ml</div>
  <div class="product-line">INULATED DOUBLE-WALL<br>STAINLESS STEEL WATER BOTTL</div>

  <div class="promise">VOLO Bottles magically<br>keeps drinks cold<br>for up to 24hrs, hot for 12</div>

  <div class="spec-label" style="left:103px; top:1060px;">diameter 8cm</div>
  <div class="spec-label" style="left:330px; top:1060px;">the whole height 27.5cm</div>
  <div class="spec-label" style="left:702px; top:1060px;">cap’s height 5.5cm</div>

</div>
</body>
</html>
```